Out of School Care Business Needs Design for Indoor Pull-Up Banner & Outdoor Footpath Sign

We provide childcare and fun activities for kids aged between 5 years old and 14 years old. Service is based within local schools. Banner will be ...

Industry/Entity Type

Business

```html
<!DOCTYPE html>
<html lang="en">
<head>
<meta charset="utf-8">
<title>Play Harbour – Footpath Sign</title>
<link rel="stylesheet" href="https://fonts.googleapis.com/css2?family=Rubik:wght@700;900&family=Montserrat:wght@600;800&display=swap">
<style>
  :root {
    --bg: #f4f4f4;
    --panel: #232323;
    --yellow: #fff200;
    --magenta: #e6007e;
    --cyan: #14a7e0;
    --white: #ffffff;
    --ink: #1a1a1a;
    --photo-a: #c9a58a;
    --photo-b: #7d8a9a;
    --photo-c: #d86a8f;
  }
  * { box-sizing: border-box; margin: 0; padding: 0; }
  html, body { width: 1200px; height: 963px; overflow: hidden; background: var(--bg); }
  .sign {
    position: absolute; left: 320px; top: 31px;
    width: 560px; height: 900px;
    background: var(--panel);
    overflow: hidden;
    font-family: "Montserrat", sans-serif;
  }
  .brand {
    position: absolute; top: 42px; left: 0; right: 0;
    display: flex; justify-content: center; align-items: center; gap: 10px;
  }
  .brand-dot { width: 26px; height: 26px; border-radius: 50%; background: var(--magenta); }
  .brand-name { font-weight: 800; font-size: 30px; color: var(--magenta); }
  .headline {
    position: absolute; top: 110px; left: 0; right: 0; text-align: center;
    font-family: "Rubik", sans-serif; font-weight: 900; font-size: 68px;
    color: var(--yellow); letter-spacing: 1px;
  }
  .tagline {
    position: absolute; top: 200px; left: 0; right: 0; text-align: center;
    font-family: "Rubik", sans-serif; font-weight: 700; font-size: 31px; color: var(--white);
  }
  .services { position: absolute; top: 262px; left: 70px; width: 420px; list-style: none; }
  .services li {
    height: 30px; border-radius: 15px; margin-bottom: 8px;
    text-align: center; line-height: 30px; font-weight: 600; font-size: 17px; color: var(--ink);
  }
  .services .pink { background: var(--magenta); }
  .services .blue { background: var(--cyan); }
  .services .gold { background: var(--yellow); }
  .feature { position: absolute; top: 380px; left: 0; }
  .activities {
    position: absolute; top: 730px; left: 0; right: 0;
    display: flex; justify-content: space-around; padding: 0 28px;
  }
  .activity {
    width: 140px; height: 106px; border-radius: 50%;
    border: 6px solid; 
  }
  .activity.pink { border-color: var(--magenta); background: linear-gradient(160deg, #8fb0d0, #6b4a3e); }
  .activity.blue { border-color: var(--cyan); background: linear-gradient(160deg, #7fa36a, #9ec9e6); }
  .activity.gold { border-color: var(--yellow); background: linear-gradient(160deg, #8aa07c, #c2b49a); }
  .web {
    position: absolute; top: 855px; left: 0; right: 0;
    display: flex; justify-content: center; align-items: center; gap: 16px;
    color: var(--white); font-weight: 600; font-size: 24px; letter-spacing: 1px;
  }
</style>
</head>
<body>
  <main class="sign">
    <div class="brand">
      <span class="brand-dot"></span>
      <span class="brand-name">Play Harbour</span>
    </div>
    <h1 class="headline">Play Harbour</h1>
    <p class="tagline">Letting Kids Be Kids</p>
    <ul class="services">
      <li class="pink">Before and after School Care</li>
      <li class="blue">School Holiday Programmes</li>
      <li class="gold">Make Your School Play Harbour Cool</li>
    </ul>

    <svg class="feature" width="560" height="350" viewBox="0 0 560 350">
      <defs>
        <linearGradient id="kidsTone" x1="0" y1="0" x2="1" y2="1">
          <stop offset="0" stop-color="var(--photo-a)"/>
          <stop offset="0.5" stop-color="var(--photo-c)"/>
          <stop offset="1" stop-color="var(--photo-b)"/>
        </linearGradient>
      </defs>
      <path role="img" aria-label="Photo of happy children playing together in a classroom"
            d="M0 70 Q280 160 560 60 L560 350 L0 350 Z" fill="url(#kidsTone)"/>
      <path d="M0 60 Q280 150 560 50 L560 66 Q280 166 0 72 Z" fill="var(--cyan)"/>
      <path d="M0 330 Q300 280 560 345 L560 350 L0 350 Z" fill="var(--magenta)"/>
    </svg>
    <div style="position:absolute;top:728px;left:0;width:560px;height:172px;background:var(--panel);"></div>

    <div class="activities">
      <div class="activity pink" role="img" aria-label="Photo of a child on a playground climbing frame"></div>
      <div class="activity blue" role="img" aria-label="Photo of children splashing in a pool"></div>
      <div class="activity gold" role="img" aria-label="Photo of kids playing games outdoors"></div>
    </div>

    <div class="web">
      <svg width="28" height="28" viewBox="0 0 28 28" fill="none" stroke="var(--white)" stroke-width="2">
        <circle cx="14" cy="14" r="12"/>
        <ellipse cx="14" cy="14" rx="5" ry="12"/>
        <line x1="2" y1="14" x2="26" y2="14"/>
        <line x1="4" y1="8" x2="24" y2="8"/>
        <line x1="4" y1="20" x2="24" y2="20"/>
      </svg>
      <span>playharbour.co.nz</span>
    </div>
  </main>
</body>
</html>
```